Brightline Tech Partners Website Design

I have here a website mockup. If you need anything further please feel free to reach out to me! Thank you!

Current site: http://brightlinetechpartners.example/

We want it clean, concise and eye catching.

Menu: I want the same idea we used from pellaroweb.example with the logo in the middle and in the menu:

Home, About Us, How Can We Help?, Media, Blog, Contact Us.

Let's have the Social Media icons at the very top please.

For the banner - we want a imagevault chess image sort of like imagevault photo 122579353 or 77865526

I want the words "Plan Ahead, Work Smarter, Stay Strong" to come in one at a time and then "Brightline Tech Partners" to show up on the banner.

Maybe have "Grow Your Business with Managed IT Services from Brightline Tech Partners" somewhere permanently on the banner that still suits everything.

Services Section: Maybe we can have them as chess pieces with something along the lines of "Make Your Next Move" - Managed IT Services, New Jersey Cloud Computing, Protect Your Business Data, Managed Email Solutions (Background 514558306)

Next Area: What sets us apart?/Testimonials (I want this as a split area) (Can we please use the banner image paralex here?)

(This is for the What Sets Us Apart side)
Outsmart threats before they reach your networks.

Outperform with the newest and latest technologies to not only keep you up and running, but to keep you at an advantage.

Outlast by embracing Business Continuity with Brightline Tech Partners by your side. (I will let you choose the background for here!)

Next Area: Book Your Free Two-Hour Review! (I want a form similar to the one on the old site.)

Next area: Blogs/Sign Up for our newsletter! (Again, please choose a relevant background)

Next Area:Contact Us area with service pages. I really like the contact us part in dorvaly.example where it shows the geographical area.

Target Market(s)

Business Owners in New Jersey looking to outsource their business IT, computer and network support.

Industry/Entity Type

Information Technology

Number of Pages Required

1 page

Font styles to use
Sans Serif

Requirements
Must have
• We want this website to be very sharp. I like bright colors, creative imagery.
• In the footer I must have @ 2016 Brightline Tech Partners | Privacy Policy | Sitemap
Should not have
• I am not a fan of stuffing everything in and making it very busy. I would like clean and professional

```html
<!DOCTYPE html>
<html lang="en">
<head>
<meta charset="utf-8">
<title>Brightline Tech Partners</title>
<link href="https://fonts.googleapis.com/css2?family=Open+Sans:ital,wght@0,400;0,600;0,700;0,800;1,400;1,600&family=Roboto:wght@300;400;500;700&display=swap" rel="stylesheet">
<style>
:root{
  --blue:#2b9ad6;
  --blue-dark:#1f7fb8;
  --ink:#333;
  --grey:#666;
  --light:#ececec;
  --line:#d6d6d6;
  --white:#fff;
  --navy:#17294a;
  --red:#d9342b;
  --steel:#8fa3b5;
}
*{box-sizing:border-box;margin:0;padding:0}
html,body{width:1200px;height:3435px;overflow:hidden}
body{position:relative;background:var(--white);font-family:"Open Sans",sans-serif;color:var(--ink)}
.abs{position:absolute}
.center{text-align:center}

/* header */
.site-header{left:0;top:0;width:1200px;height:73px;background:var(--white);z-index:3}
.nav a{position:absolute;top:30px;font-size:12px;color:var(--grey);text-decoration:none;letter-spacing:.3px}
.nav a.active{color:var(--blue)}
.logo-tab{left:430px;top:60px;z-index:2}
.brand{left:430px;top:22px;width:340px;text-align:center;font-weight:700;font-size:19px;color:#3a3a3a;z-index:4;white-space:nowrap}
.brand-mark{display:inline-block;width:30px;height:30px;border-radius:50%;background:var(--steel);margin-right:8px;vertical-align:-8px}
.socials{left:1040px;top:6px;display:flex;gap:6px}
.socials span{width:24px;height:24px;border-radius:50%;background:var(--blue)}
.socials span:nth-child(3){background:var(--red)}

/* hero */
.hero{left:0;top:73px;width:1200px;height:534px;background:linear-gradient(160deg,#6b5e52 0%,#3a3430 40%,#2a2623 70%,#5a5048 100%)}
.hero h1{position:absolute;left:0;top:135px;width:1200px;font-size:37px;font-weight:700;color:var(--white);letter-spacing:1px;text-shadow:0 2px 4px rgba(0,0,0,.5)}
.hero h2{position:absolute;left:0;top:200px;width:1200px;font-size:44px;font-weight:600;color:var(--white);letter-spacing:3px;text-shadow:0 2px 4px rgba(0,0,0,.5)}
.btn-primary{background:var(--blue);color:var(--white);font-weight:700;font-size:19px;letter-spacing:1px;border-radius:3px}
.hero .btn-primary{position:absolute;left:515px;top:295px;width:170px;height:38px;line-height:38px;text-align:center}
.hero p{position:absolute;left:0;top:395px;width:1200px;font-size:27px;font-weight:700;color:var(--white);line-height:39px;text-shadow:0 2px 4px rgba(0,0,0,.6)}

/* services */
.services{left:0;top:607px;width:1200px;height:515px;background:linear-gradient(#f1f1f1,#e1e1e1)}
.chess-row{left:490px;top:18px;width:220px;height:68px;background:linear-gradient(#f0c99a,#c98b4f);border-radius:6px 6px 2px 2px}
.services .kicker{left:0;top:98px;width:1200px;font-size:15px;font-weight:600;color:#444}
.service{top:150px;width:300px;height:250px;text-align:center}
.service + .service{border-left:1px solid var(--line)}
.service svg{display:block;margin:40px auto 0}
.service h3{font-weight:400;font-size:22px;line-height:28px;color:#3d3d3d;margin-top:22px}

/* apart + testimonials */
.apart{left:0;top:1122px;width:1200px;height:497px;background:linear-gradient(100deg,#2e2b29 0%,#4c4540 35%,#2b2826 60%,#191817 100%)}
.apart h2{position:absolute;font-size:28px;font-weight:700;color:var(--white)}
.accordion{left:57px;width:468px}
.acc-head{height:48px;border-radius:6px 6px 0 0;background:var(--blue);border:2px solid #7cc6ee;color:var(--white);font-size:20px;padding:10px 18px;position:relative}
.acc-head.closed{border-radius:6px;height:42px;padding:7px 18px}
.acc-head::after{content:"";position:absolute;right:22px;top:19px;border:6px solid transparent}
.acc-head.open::after{border-bottom-color:var(--white);top:13px}
.acc-head.closed::after{border-top-color:var(--white);top:17px}
.acc-body{height:185px;background:rgba(190,190,190,.82);border:2px solid #7cc6ee;border-top:0;border-radius:0 0 6px 6px;padding:12px 14px;font-size:12.5px;line-height:20px;color:#333}
.testimonial{left:650px;width:490px;color:var(--white)}
.testimonial .sub{font-size:12px;letter-spacing:.5px}
.testimonial .lead{font-size:18px}
.testimonial blockquote{font-style:italic;font-weight:600;font-size:15px;line-height:20px}
.testimonial .who{text-align:right;font-size:12.5px}
.testimonial .org{text-align:right;font-size:10px;color:#6cc0ef}
.dots span{display:inline-block;width:20px;height:20px;border-radius:50%;border:2px solid #aaa;background:#3a3a3a;margin-right:8px}

/* review */
.review h2{left:0;top:1648px;width:1200px;font-size:25px;font-weight:400;color:#333}
.review-card{left:96px;top:1730px;width:1041px;height:382px;border:2px solid #ddd;border-radius:10px;box-shadow:0 2px 8px rgba(0,0,0,.08);background:var(--white)}
.pitch{left:55px;top:22px;width:250px;text-align:center}
.pitch .q{font-family:"Roboto",sans-serif;font-weight:300;font-size:32px;line-height:36px;color:#555}
.pitch .a{font-family:"Roboto",sans-serif;font-weight:700;font-size:24px;line-height:30px;color:var(--blue-dark);margin-top:18px}
.sign-photo{left:373px;top:0;width:296px;height:322px;background:linear-gradient(#2f64b8 0%,#234f95 40%,#e4e4e4 41%,#f2f2f2 100%)}
.form{left:700px;top:28px;width:298px;font-family:"Roboto",sans-serif}
.form h3{font-weight:400;font-size:22px;color:var(--blue-dark)}
.form .hint{font-size:13px;color:#888;margin-bottom:14px}
.field{height:27px;border:2px solid var(--blue);border-radius:2px;font-size:11px;color:#555;padding:4px 8px;margin-bottom:19px;position:relative}
.field b{color:var(--red);font-weight:400}
.field.select::after{content:"";position:absolute;right:8px;top:8px;border:5px solid transparent;border-top-color:#333}
.submit{margin:2px 0 0 86px;width:104px;height:22px;line-height:22px;text-align:center;font-size:12px;font-weight:700;letter-spacing:1px;color:var(--white);background:var(--blue)}

/* blog */
.blog{left:0;top:2164px;width:1200px;height:602px;background:var(--light)}
.blog h2{left:0;top:80px;width:1200px;font-size:26px;font-weight:600;color:#444}
.blog h2::after{content:"";display:block;width:64px;height:3px;background:var(--blue);margin:6px auto 0}
.post{left:96px;width:1031px;height:164px;background:var(--white)}
.post-img{left:0;top:0;width:324px;height:164px}
.post-body{left:333px;top:0;width:698px;height:164px;border-left:2px solid var(--blue);padding:12px 30px 0 18px}
.post-date{font-size:11px;color:#888}
.post-date::before{content:"";display:inline-block;width:16px;height:10px;background:#bbb;margin-right:8px}
.post h3{font-size:15px;font-weight:400;color:var(--blue-dark);margin:8px 0 6px}
.post p{font-size:12px;line-height:19px;color:#777}
.read-more{position:absolute;right:48px;bottom:12px;border:1px solid var(--blue);color:var(--blue);font-size:10px;padding:2px 14px}

/* newsletter */
.newsletter{left:0;top:2766px;width:1200px;height:302px;background:linear-gradient(#1e2224,#2c3236 60%,#121416)}
.newsletter h2{left:0;top:32px;width:1200px;font-size:19px;font-weight:700;color:var(--white)}
.newsletter p{left:215px;top:80px;width:770px;font-size:12px;line-height:22px;color:var(--white);font-weight:600}
.subscribe{left:244px;top:188px;width:713px;height:43px;display:flex;border-radius:2px;overflow:hidden}
.subscribe .input{flex:1;background:rgba(40,40,40,.7);border:1px solid #ddd;color:#eee;font-size:13px;padding:12px}
.subscribe .go{width:182px;background:var(--blue);color:var(--white);font-size:14px;line-height:43px;text-align:center}

/* contact */
.contact{left:0;top:3068px;width:1200px;height:310px;background:radial-gradient(ellipse at 55% 50%,#2e4e7e 0%,#1b3257 50%,#0f1e38 100%)}
.contact h2{left:0;top:28px;width:1200px;font-size:34px;font-weight:700;color:var(--white);letter-spacing:2px}
.contact .brand-foot{left:144px;top:110px;font-size:19px;font-weight:700;color:var(--white)}
.contact .lines{left:144px;top:174px;font-size:13px;line-height:29px;color:var(--white)}
.contact .lines svg{vertical-align:-2px;margin-right:8px}
.pin-label{left:640px;top:165px;font-size:10px;color:var(--white)}
.menu-foot{right:70px;top:108px;text-align:right;color:var(--white)}
.menu-foot h3{font-size:17px;font-weight:700;margin-bottom:14px}
.menu-foot li{list-style:none;font-size:11.5px;line-height:23.5px}

/* footer */
.site-footer{left:0;top:3378px;width:1200px;height:57px;background:#0d0d0d;color:#ccc;font-size:12px}
.site-footer .copy{left:134px;top:20px}
.site-footer .icons{right:70px;top:19px;display:flex;gap:12px}
.site-footer .icons span{width:18px;height:18px;background:#888;border-radius:50%}
</style>
</head>
<body>

<header class="site-header abs">
  <nav class="nav">
    <a href="#" class="active" style="left:135px">HOME</a>
    <a href="#" style="left:210px">ABOUT US</a>
    <a href="#" style="left:314px">HOW CAN WE HELP</a>
    <a href="#" style="left:772px">MEDIA</a>
    <a href="#" style="left:852px">BLOG</a>
    <a href="#" style="left:922px">CONTACT US</a>
  </nav>
  <div class="socials abs"><span></span><span></span><span></span><span></span></div>
</header>
<svg class="logo-tab abs" width="340" height="45" viewBox="0 0 340 45"><path d="M0 0 H340 C300 0 290 38 170 40 C50 38 40 0 0 0Z" fill="#fff"/></svg>
<div class="brand abs"><span class="brand-mark"></span>Brightline Tech Partners</div>

<section class="hero abs" role="img" aria-label="Close-up photo of a hand moving a chess piece on a board among pawns and knights">
  <h1 class="center">PLAN AHEAD... WORK SMARTER... STAY STRONG</h1>
  <h2 class="center">BRIGHTLINE TECH PARTNERS</h2>
  <div class="btn-primary">KNOW MORE</div>
  <p class="center">GROW YOUR BUSINESS WITH MANAGED<br>IT SERVICES FROM BRIGHTLINE TECH PARTNERS</p>
</section>

<section class="services abs">
  <div class="chess-row abs" role="img" aria-label="Row of wooden chess pieces"></div>
  <div class="kicker abs center">MAKE YOUR NEXT MOVE</div>
  <div class="service abs" style="left:0">
    <svg width="100" height="80" viewBox="0 0 100 80"><path d="M22 62a16 16 0 0 1 4-31 22 22 0 0 1 42-4 17 17 0 0 1 10 35Z" fill="#2b9ad6"/><circle cx="50" cy="46" r="9" fill="#fff"/><circle cx="50" cy="46" r="4" fill="#2b9ad6"/></svg>
    <h3>Managed IT<br>Services</h3>
  </div>
  <div class="service abs" style="left:300px">
    <svg width="100" height="80" viewBox="0 0 100 80"><path d="M22 62a16 16 0 0 1 4-31 22 22 0 0 1 42-4 17 17 0 0 1 10 35Z" fill="none" stroke="#2b9ad6" stroke-width="4"/><circle cx="60" cy="60" r="10" fill="#2b9ad6"/><circle cx="60" cy="60" r="4" fill="#fff"/></svg>
    <h3>New Jersey<br>Cloud Computing</h3>
  </div>
  <div class="service abs" style="left:600px">
    <svg width="100" height="80" viewBox="0 0 100 80"><path d="M36 36v-10a14 14 0 0 1 28 0v10" fill="none" stroke="#2b9ad6" stroke-width="6"/><rect x="28" y="36" width="44" height="40" rx="5" fill="#2b9ad6"/><circle cx="50" cy="52" r="5" fill="#fff"/><rect x="48" y="54" width="4" height="12" fill="#fff"/></svg>
    <h3>Protect Your<br>Business Data</h3>
  </div>
  <div class="service abs" style="left:900px">
    <svg width="100" height="80" viewBox="0 0 100 80"><rect x="24" y="22" width="62" height="42" fill="none" stroke="#2b9ad6" stroke-width="4"/><path d="M24 22l31 24 31-24" fill="none" stroke="#2b9ad6" stroke-width="4"/><path d="M6 36h14M10 46h10M4 56h16" stroke="#2b9ad6" stroke-width="3"/></svg>
    <h3>Managed Email<br>Solutions</h3>
  </div>
</section>

<section class="apart abs" role="img" aria-label="Dark photo of a hand moving a chess knight on a board">
  <h2 style="left:133px;top:40px">WHAT SETS US APART?</h2>
  <div class="accordion abs" style="top:93px">
    <div class="acc-head open">Outsmart</div>
    <div class="acc-body">Outsmart threats before they reach your networks. Lorem Ipsum is simply dummy text of the printing and typesetting industry. Lorem Ipsum has been the industry's standard dummy text ever since the 1500s, when an unknown printer took a galley of type and scrambled it to make a type specimen book. It has survived not only five centuries, but also the leap into electronic typesetting, remaining essentially unchanged.</div>
  </div>
  <div class="accordion abs" style="top:348px"><div class="acc-head closed">Outperform</div></div>
  <div class="accordion abs" style="top:411px"><div class="acc-head closed">Outperform</div></div>

  <div class="testimonial abs" style="top:46px">
    <h2 style="position:static;text-align:center;font-size:27px">TESTIMONIALS</h2>
    <div class="sub center" style="margin-top:18px">WHAT PEOPLE ARE SAYING</div>
    <div class="lead" style="margin-top:30px">Incredible value and peace of mind</div>
    <blockquote style="margin-top:14px">“Brightline Tech Partners’ “Virtual IT” Management Services provide us with insight into the health of our network something we couldn’t quantify in the past. The remote monitoring capabilities help us identify small issues before they become major problems and save time and money by anticipating server upgrades. Brightline’s “Virtual IT” Management Services provide us with incredible value and peace of mind.”</blockquote>
    <div class="who" style="margin-top:12px">Daniel Arlow</div>
    <div class="org">Harborline Lending, Clifton NJ</div>
    <div class="dots center" style="margin-top:44px"><span></span><span></span></div>
  </div>
</section>

<section class="review">
  <h2 class="abs center">Book Your Free Review</h2>
  <div class="review-card abs">
    <div class="pitch abs">
      <div class="q">Tired Of Your Old IT Company Giving You The Run Around?</div>
      <div class="a">Experience Brightline Tech Partners. Book Your Free 2-Hour IT Review!</div>
    </div>
    <div class="sign-photo abs" role="img" aria-label="Photo of a businessman in a blue shirt holding a sign reading Get Started Today"></div>
    <div class="form abs">
      <h3>Get Started Now!</h3>
      <div class="hint">Send in Your Information Below.</div>
      <div class="field">Full Name <b>*</b></div>
      <div class="field">Company <b>*</b></div>
      <div class="field">Phone</div>
      <div class="field">Email <b>*</b></div>
      <div class="field select">How can our team help you? <b>*</b></div>
      <div class="submit">SUBMIT</div>
    </div>
  </div>
</section>

<section class="blog abs">
  <h2 class="abs center">Our Blog</h2>
  <article class="post abs" style="top:159px">
    <div class="post-img abs" role="img" aria-label="Photo of hands holding a glowing blue digital cloud" style="background:linear-gradient(120deg,#0e2440,#2a5c93 50%,#0c1a2e)"></div>
    <div class="post-body abs">
      <div class="post-date">12 November 2015</div>
      <h3>Cloud Security Risks Mostly Come from Employees</h3>
      <p>With so many companies and organizations moving a majority of their data networks to the cloud, there is an often-overlooked and underestimated danger in the midst of this exodus to cloud computing: risk of cyber security breach from within. And, while it is not something owners or executives want to face when busy with ...</p>
      <span class="read-more">READ MORE</span>
    </div>
  </article>
  <article class="post abs" style="top:366px">
    <div class="post-img abs" role="img" aria-label="Photo of a padlock resting on a laptop keyboard" style="background:linear-gradient(120deg,#e6e6e6,#9a9a9a 50%,#3a3a3a)"></div>
    <div class="post-body abs">
      <div class="post-date">21 June 2015</div>
      <h3>Recent Entries to the Health Breach Tool Show Continued Increase in Cyber Threat</h3>
      <p>The federal health agency has made some new entries recently to its data breach tool listings. The first of these is Northfield Wellness Clinic, a data breach that has reportedly affected nearly 2,000 patients. The second of these was awarded to Crestview Family Physicians of Brookside, ...</p>
      <span class="read-more">READ MORE</span>
    </div>
  </article>
</section>

<section class="newsletter abs" role="img" aria-label="Dim photo of a desk with a monitor and speakers">
  <h2 class="abs center">Subscribe to Newsletter</h2>
  <p class="abs center">Lorem Ipsum is simply dummy text of the printing and typesetting industry. Lorem Ipsum has been the industry's standard dummy text ever since the 1500s, when an unknown printer took a galley of type and scrambled it to make a type specimen book.</p>
  <div class="subscribe abs"><div class="input">Enter you Email......</div><div class="go">Subscribe</div></div>
</section>

<section class="contact abs" role="img" aria-label="Dark blue world map showing the office location">
  <h2 class="abs center">Get in Touch !</h2>
  <div class="brand-foot abs">Brightline Tech Partners</div>
  <div class="lines abs">
    <div>48 Maple Ridge Road, Linden Vale NJ 07199</div>
    <div><svg width="12" height="12" viewBox="0 0 12 12"><path d="M2 1h3l1 3-2 1a7 7 0 0 0 3 3l1-2 3 1v3c-6 0-9-3-9-9z" fill="#fff"/></svg>(555) 014-2290</div>
    <div><svg width="13" height="10" viewBox="0 0 13 10"><rect width="13" height="10" fill="#fff"/><path d="M0 0l6.5 5L13 0" fill="none" stroke="#1b3257"/></svg>hello@brightlinetechpartners.example</div>
  </div>
  <svg class="abs" style="left:612px;top:150px" width="18" height="26" viewBox="0 0 18 26"><path d="M9 26S0 14 0 9a9 9 0 0 1 18 0c0 5-9 17-9 17z" fill="#d9342b"/><circle cx="9" cy="9" r="3.5" fill="#fff"/></svg>
  <div class="pin-label abs">48 Maple Ridge Rd</div>
  <div class="menu-foot abs">
    <h3>Access Menus</h3>
    <ul><li>HOME</li><li>ABOUT US</li><li>HOW CAN WE HELP</li><li>MEDIA</li><li>BLOG</li><li>CONTACT US</li></ul>
  </div>
</section>

<footer class="site-footer abs">
  <div class="copy abs">Copyright © 2016 Brightline Tech Partners.&nbsp; All Rights Reserved</div>
  <div class="icons abs"><span></span><span></span><span></span><span></span><span></span></div>
</footer>

</body>
</html>
```